Bright Smile Dental*

Promotion for a new dental office
brghtsmlvoranta.com

I just opened a new dental office and would like to promote my office to
the public. I attached some examples. I have AI files for logo and also can
provide office pictures. Website is brightsmilevoranta.com.

Target Market(s)

General public

Requirements
Must have
• Dr. Tovin
• Halvern State, BS, MCB
• Marwick School of Dentistry
• US Army veteran
• New patient exam, X-rays and basic cleaning for $95.
• White background
• 20% discount with this post card. This only applied to private pay patients(in fine print)
• Open saturdays and evenings
Should not have
• No postal info. Not going to mail this out.

```html
<!DOCTYPE html>
<html lang="en">
<head>
<meta charset="utf-8">
<title>Bright Smile Dental – Promotion Cards</title>
<link href="https://fonts.googleapis.com/css2?family=Questrial&family=Roboto+Condensed:wght@400&family=Ubuntu:wght@400;500&family=Oswald:wght@400;500&family=Open+Sans:wght@600;700&display=swap" rel="stylesheet">
<style>
:root{
  --teal:#14a3b8;
  --teal-dark:#137f93;
  --teal-deep:#0f6f82;
  --ink:#4a4a4a;
  --ink-dark:#333;
  --grey-soft:#e6e7e8;
  --paper:#ffffff;
  --stage:#e8e8e8;
}
*{box-sizing:border-box;margin:0;padding:0}
html,body{width:1120px;height:1200px;overflow:hidden;background:var(--stage)}
.card{position:absolute;left:40px;width:1040px;height:560px;background:var(--paper);overflow:hidden;box-shadow:0 3px 10px rgba(0,0,0,.25)}
.card--offer{top:30px}
.card--practice{top:620px}
.card-art{position:absolute;inset:0;width:1040px;height:560px}
.abs{position:absolute}

.brand{position:absolute;left:28px;top:28px;display:flex;align-items:center}
.brand-mark{width:96px;height:96px;border:2px solid #6d6e70;border-radius:50%;flex:none}
.brand-text{margin-left:14px}
.brand-name{font-family:'Questrial',sans-serif;font-size:33px;color:#58595b;letter-spacing:0;line-height:1;white-space:nowrap}
.brand-tag{font-family:'Roboto Condensed',sans-serif;font-size:22px;color:#58595b;margin-top:12px;letter-spacing:.3px;padding-left:12px}

.ribbon{position:absolute;left:0;height:36px;background:var(--teal-dark);color:#fff;font-family:'Ubuntu',sans-serif;font-size:21px;line-height:36px;clip-path:polygon(0 0,100% 0,97% 100%,0 100%)}

.services{position:absolute;top:192px;font-family:'Ubuntu',sans-serif;font-size:14.5px;color:var(--ink);list-style:none;line-height:22.5px}
.services li::before{content:"• ";color:var(--teal-dark)}

.offer{position:absolute;top:305px;height:116px;border:2px solid var(--teal-dark);border-radius:8px;color:var(--teal-dark);font-family:'Oswald',sans-serif}
.offer-big{position:absolute;font-size:64px;line-height:1;letter-spacing:-2px;transform:scaleX(.8);transform-origin:left}
.offer-lines{position:absolute;font-size:17px;line-height:24px;transform:scaleX(.85);transform-origin:left}
.offer-fine{position:absolute;left:0;right:0;bottom:6px;text-align:center;font-family:'Ubuntu',sans-serif;font-size:12px;color:var(--ink)}

.motto{font-family:'Open Sans',sans-serif;font-weight:700;font-size:20px;color:var(--teal-dark);white-space:nowrap}
.address{font-family:'Ubuntu',sans-serif;font-size:17.5px;color:var(--teal-dark);line-height:24px}

.badge-text{position:absolute;width:120px;text-align:center;color:#fff;font-family:'Ubuntu',sans-serif;font-size:18px;line-height:25px}

.cta-small{font-family:'Open Sans',sans-serif;font-weight:700;font-size:14.5px;color:#fff;white-space:nowrap}
.cta-phone{display:flex;align-items:center;gap:8px;font-family:'Ubuntu',sans-serif;font-size:38px;line-height:44px;color:#fff;letter-spacing:1.5px;white-space:nowrap}
.cta-web{font-family:'Open Sans',sans-serif;font-weight:700;font-size:13.5px;color:#fff;white-space:nowrap}

.checks{position:absolute;left:33px;top:187px;list-style:none;font-family:'Ubuntu',sans-serif;font-size:20px;color:var(--ink-dark);line-height:32px}
.checks li{display:flex;align-items:center;gap:12px}
.tick{width:18px;height:18px;border-radius:50%;background:var(--teal);color:#fff;font-size:12px;line-height:18px;text-align:center;font-weight:700}

.doctor{position:absolute;left:35px;top:344px;font-family:'Ubuntu',sans-serif;color:var(--ink-dark)}
.doctor-name{font-family:'Open Sans',sans-serif;font-weight:700;font-size:21px;color:var(--teal-dark);margin-bottom:6px}
.doctor p{font-size:17.5px;line-height:25px}

.map-label{position:absolute;left:705px;top:208px;width:313px;height:36px;background:var(--teal-dark);color:#fff;font-family:'Ubuntu',sans-serif;font-size:17px;line-height:38px;text-align:center}
.map{position:absolute;left:663px;top:234px;width:355px;height:158px;border:3px solid var(--teal-dark);border-radius:8px;background:linear-gradient(135deg,#eef0f1,#e2e5e7);overflow:hidden}
</style>
</head>
<body>

<!-- Offer card -->
<section class="card card--offer">
  <svg class="card-art" viewBox="0 0 1040 560" aria-hidden="true">
    <defs>
      <linearGradient id="offerPhoto" x1="0" y1="0" x2="1" y2="1">
        <stop offset="0" stop-color="#dfeef6"/>
        <stop offset=".55" stop-color="#d8c3b4"/>
        <stop offset="1" stop-color="#9aa3ab"/>
      </linearGradient>
      <linearGradient id="fadeLeft" x1="0" y1="0" x2="1" y2="0">
        <stop offset="0" stop-color="#ececed"/>
        <stop offset="1" stop-color="#ffffff"/>
      </linearGradient>
    </defs>
    <rect width="1040" height="560" fill="url(#fadeLeft)"/>
    <path d="M0 470 Q220 440 470 500 L470 560 L0 560Z" fill="#ffffff"/>
    <path d="M0 445 Q240 425 470 470 L470 488 Q240 444 0 462Z" fill="#d9dadb"/>
  </svg>
  <svg class="card-art" viewBox="0 0 1040 560" role="img" aria-label="Photo of a smiling young couple embracing outdoors">
    <path d="M640 0 L1040 0 L1040 560 L535 560 Q455 300 640 0Z" fill="url(#offerPhoto)"/>
  </svg>
  <svg class="card-art" viewBox="0 0 1040 560" aria-hidden="true">
    <path d="M640 0 Q455 300 535 560" fill="none" stroke="var(--teal-dark)" stroke-width="9"/>
    <path d="M440 560 Q700 400 1040 426 L1040 560Z" fill="#ffffff"/>
    <path d="M470 560 Q700 420 1040 440 L1040 560Z" fill="var(--teal)"/>
    <circle cx="373" cy="491" r="55" fill="var(--teal-dark)"/>
    <circle cx="373" cy="491" r="58" fill="none" stroke="var(--teal-dark)" stroke-width="7" stroke-dasharray="7.6 7.6"/>
  </svg>

  <div class="brand">
    <div class="brand-mark"></div>
    <div class="brand-text">
      <div class="brand-name">BRIGHT SMILE DENTAL</div>
      <div class="brand-tag">MODERN GENERAL DENTISTRY</div>
    </div>
  </div>

  <div class="ribbon" style="top:139px;width:265px;padding-left:22px">OUR SERVICES</div>

  <ul class="services" style="left:27px">
    <li>Exams &amp; cleanings</li>
    <li>Dental fillings</li>
    <li>Cosmetic dentistry</li>
    <li>Periodontal (gum) care</li>
    <li>Crowns &amp; bridges</li>
  </ul>
  <ul class="services" style="left:240px">
    <li>Same day treatment</li>
    <li>Root canal therapy</li>
    <li>Night guard</li>
    <li>Tooth extracrions</li>
    <li>Emergency care</li>
  </ul>

  <div class="offer" style="left:30px;width:213px">
    <div class="offer-big" style="left:10px;top:18px">$95</div>
    <div class="offer-lines" style="left:90px;top:16px">EXAM<br>X-RAY<br>BASIC CLEANING</div>
  </div>
  <div class="offer" style="left:252px;width:211px">
    <div class="offer-big" style="left:12px;top:12px">20%</div>
    <div class="offer-lines" style="left:115px;top:14px">OFF<br>ON<br>TREATMENTS</div>
    <div class="offer-fine">only applies to private pay pts.</div>
  </div>

  <div class="abs motto" style="left:32px;top:470px">ONE OF A KIND SMILE.</div>
  <div class="abs address" style="left:35px;top:503px">412 N. Linden Road Ste #10<br>Voranta, Texas 78000</div>

  <div class="badge-text" style="left:313px;top:466px">SE HABLA<br>ESPAÑOL!</div>

  <div class="abs cta-small" style="right:20px;top:466px">SCHEDULE YOUR APPOINTMENT TODAY!</div>
  <div class="abs cta-phone" style="right:20px;top:483px">
    <svg width="34" height="34" viewBox="0 0 34 34" aria-hidden="true"><circle cx="17" cy="17" r="15" fill="none" stroke="#fff" stroke-width="2.5"/><path d="M11 9c1-1 2-1 3 0l2 3c.5 1 0 2-1 2.5-.5.5 0 2 1.5 3.5s3 2 3.5 1.5c.5-1 1.5-1.5 2.5-1l3 2c1 1 1 2 0 3-2 2-5 2-9-2s-4.5-9-2.5-12.5z" fill="#fff"/></svg>
    555-014-2870
  </div>
  <div class="abs cta-web" style="right:20px;top:530px">www.Brightsmilevoranta.com &nbsp;|&nbsp; etovin907@brightmail.com</div>
</section>

<!-- Practice card -->
<section class="card card--practice">
  <svg class="card-art" viewBox="0 0 1040 560" aria-hidden="true">
    <defs>
      <linearGradient id="practiceBg" x1="0" y1="0" x2="1" y2="0">
        <stop offset="0" stop-color="#e3e4e5"/>
        <stop offset=".6" stop-color="#f7f7f7"/>
        <stop offset="1" stop-color="#ffffff"/>
      </linearGradient>
      <linearGradient id="familyPhoto" x1="0" y1="0" x2="1" y2="1">
        <stop offset="0" stop-color="#f1e3df"/>
        <stop offset=".5" stop-color="#dcc2b4"/>
        <stop offset="1" stop-color="#a9c3dc"/>
      </linearGradient>
      <radialGradient id="exam" cx=".5" cy=".5" r=".6">
        <stop offset="0" stop-color="#e8b8ae"/>
        <stop offset=".6" stop-color="#e9d6d0"/>
        <stop offset="1" stop-color="#c9dfe9"/>
      </radialGradient>
    </defs>
    <rect width="1040" height="560" fill="url(#practiceBg)"/>
    <path d="M465 0 Q640 160 660 560" fill="none" stroke="#ffffff" stroke-width="26"/>
    <path d="M495 0 Q668 170 688 560" fill="none" stroke="#b9e2ef" stroke-width="10"/>
    <path d="M688 560 Q800 470 1040 462 L1040 560Z" fill="#ffffff"/>
    <path d="M700 500 Q840 440 1040 450 L1040 468 Q850 456 715 515Z" fill="#d9dadb"/>
    <path d="M0 446 Q300 436 560 560 L0 560Z" fill="#ffffff"/>
    <path d="M0 460 Q300 452 530 560 L0 560Z" fill="var(--teal)"/>
  </svg>
  <svg class="card-art" viewBox="0 0 1040 560" role="img" aria-label="Photo of a happy family of four, parents carrying two children on their backs">
    <path d="M690 0 L1040 0 L1040 250 L665 250 Q640 120 690 0Z" fill="url(#familyPhoto)" opacity=".9"/>
  </svg>
  <svg class="card-art" viewBox="0 0 1040 560" role="img" aria-label="Close-up photo of a dental examination with mirror and probe">
    <circle cx="460" cy="329" r="127" fill="#ffffff"/>
    <circle cx="460" cy="329" r="121" fill="url(#exam)"/>
  </svg>
  <svg class="card-art" viewBox="0 0 1040 560" aria-hidden="true">
    <circle cx="553" cy="470" r="55" fill="var(--teal-dark)"/>
    <circle cx="553" cy="470" r="58" fill="none" stroke="var(--teal-dark)" stroke-width="7" stroke-dasharray="7.6 7.6"/>
  </svg>

  <div class="brand">
    <div class="brand-mark"></div>
    <div class="brand-text">
      <div class="brand-name">BRIGHT SMILE DENTAL</div>
      <div class="brand-tag">MODERN GENERAL DENTISTRY</div>
    </div>
  </div>

  <div class="ribbon" style="top:137px;width:480px;padding-left:33px">MODERN STATE OF THE ART EQUIPMENT</div>

  <ul class="checks">
    <li><span class="tick">›</span>Personalized care</li>
    <li><span class="tick">›</span>High quality care</li>
    <li><span class="tick">›</span>Patient centered</li>
    <li><span class="tick">›</span>Modern dentistry</li>
  </ul>

  <div class="doctor">
    <div class="doctor-name">Dr. Elan Tovin</div>
    <p>Halvern State, BS, MCB</p>
    <p>Marwick School of Dentistry</p>
    <p>US Army veteran</p>
  </div>

  <div class="abs cta-small" style="left:30px;top:482px">SCHEDULE YOUR APPOINTMENT TODAY!</div>
  <div class="abs cta-phone" style="left:30px;top:498px">
    <svg width="34" height="34" viewBox="0 0 34 34" aria-hidden="true"><circle cx="17" cy="17" r="15" fill="none" stroke="#fff" stroke-width="2.5"/><path d="M11 9c1-1 2-1 3 0l2 3c.5 1 0 2-1 2.5-.5.5 0 2 1.5 3.5s3 2 3.5 1.5c.5-1 1.5-1.5 2.5-1l3 2c1 1 1 2 0 3-2 2-5 2-9-2s-4.5-9-2.5-12.5z" fill="#fff"/></svg>
    555-014-2870
  </div>

  <div class="badge-text" style="left:493px;top:445px">SE HABLA<br>ESPAÑOL!</div>

  <div class="map" role="img" aria-label="Street map showing the office location"></div>
  <div class="map-label">412 LINDEN RD. VORANTA, TX 78000</div>

  <div class="abs motto" style="left:738px;top:404px">ONE OF A KIND SMILE.</div>

  <div class="abs motto" style="right:20px;top:510px">OPEN SATURDAYS AND EVENINGS</div>
  <div class="abs cta-web" style="right:20px;top:537px;color:var(--ink-dark)">www.Brightsmilevoranta.com &nbsp;|&nbsp; etovin907@brightmail.com</div>
</section>

</body>
</html>
```